KL MOTORS BANNER/SIGN DESIGN

Design a banner sign for outdoor use for KL MOTORS - a premium pre owned vehicle sales center. The size must be 36 feet in width
and 3 feet in height.

Information required: logo (attached)
-PREMIUM PRE-OWEND VEHICLE SALES
- 517.264.3081

perhaps in smaller font: BUY-SELL-TRADE

prefer white background but could possibly do red matching the logo

```html
<!DOCTYPE html>
<html lang="en">
<head>
<meta charset="utf-8">
<title>KL Motors Banner</title>
<link href="https://fonts.googleapis.com/css2?family=Roboto+Condensed:ital,wght@0,700;0,800;1,800&family=Open+Sans:wght@400&display=swap" rel="stylesheet">
<style>
  :root {
    --page-bg: #eceef1;
    --banner-white: #ffffff;
    --brand-red: #e00000;
    --accent-orange: #f0891c;
    --ink: #111111;
    --phone-red: #e3132c;
  }
  html, body {
    margin: 0;
    padding: 0;
    width: 1200px;
    height: 1000px;
    overflow: hidden;
    background: var(--page-bg);
  }
  .banner {
    position: absolute;
    left: 24px;
    top: 452px;
    width: 1152px;
    height: 96px;
    background: var(--banner-white);
    box-shadow: 0 3px 6px rgba(0,0,0,0.18);
  }
  .banner-shapes {
    position: absolute;
    inset: 0;
  }
  .brand {
    position: absolute;
    left: 14px;
    top: 0;
    height: 96px;
    display: flex;
    align-items: center;
    gap: 16px;
  }
  .brand-dot {
    width: 62px;
    height: 62px;
    border-radius: 50%;
    background: var(--brand-red);
  }
  .brand-name {
    font-family: "Roboto Condensed", sans-serif;
    font-weight: 800;
    font-size: 40px;
    letter-spacing: 2px;
    color: var(--ink);
  }
  .headline {
    position: absolute;
    left: 390px;
    width: 520px;
    top: 8px;
    text-align: center;
    color: var(--banner-white);
    font-family: "Roboto Condensed", sans-serif;
    font-weight: 800;
    line-height: 1;
  }
  .headline-top {
    display: block;
    font-size: 37px;
    letter-spacing: 1px;
  }
  .headline-bottom {
    display: block;
    margin-top: 8px;
    font-size: 33px;
    font-weight: 700;
  }
  .contact {
    position: absolute;
    left: 940px;
    width: 212px;
    top: 14px;
    text-align: center;
  }
  .contact-services {
    display: block;
    font-family: "Roboto Condensed", sans-serif;
    font-style: italic;
    font-weight: 800;
    font-size: 22px;
    color: var(--ink);
  }
  .contact-phone {
    display: block;
    margin-top: 4px;
    font-family: "Open Sans", sans-serif;
    font-size: 30px;
    color: var(--phone-red);
  }
</style>
</head>
<body>
  <div class="banner">
    <svg class="banner-shapes" width="1152" height="96" viewBox="0 0 1152 96" aria-hidden="true">
      <polygon points="399,0 919,0 882,96 378,96" fill="var(--brand-red)"/>
      <polygon points="919,0 937,0 900,96 882,96" fill="var(--accent-orange)"/>
    </svg>

    <div class="brand">
      <div class="brand-dot"></div>
      <span class="brand-name">KL MOTORS</span>
    </div>

    <div class="headline">
      <span class="headline-top">PREMIUM</span>
      <span class="headline-bottom">PRE-OWEND VEHICLE SALES</span>
    </div>

    <div class="contact">
      <span class="contact-services">BUY-SELL-TRADE</span>
      <span class="contact-phone">517.264.3081</span>
    </div>
  </div>
</body>
</html>
```